Packaging & Label Design for CDB Products

We are a European CBD company specialising in athletic recovery, sleep improvement and wellness.

We would like the packaging to incorporate our logo and name (and font 'Codec') 'Meridell CBD'. The design must be transferable to all of our products. CBD Oils, Balms, Lip Balm and Vape E-Liquid.

We would like it to be simple but eye-catching and modern. We don't want bright colours. Preferred pallet of muted greys, blacks, white and pastel colours. Geometric concepts, possibly using different colours for each item of the range, we are open to new and fresh ideas (we are seeking you for your experience) and when we find the right design we would likely throw more work in your direction..

Our product range is not complete so the designer must be flexible with some changes and provide files where format can be easily edited by packaging manufacturer. We are also waiting for dimensions for the labels and boxes for several products and will supply the designer with full dimensions of all products once selected.

Oil Box: 2.6 x 9.0 x 2.6 cm (open format 16.7 x 11.6cm)
Labels: 7.8 x 3.3 cm (Front and Back)

Our expected product range will be:
CBD Oil 1000mg
CBD Oil 3000mg
CBD Balm 100mg
CBD Balm 300mg
E-Liquid 500mg
Lip Balm 50mg

We look forward to seeing your ideas.

Best Regards
Meridell CBD

```html
<!DOCTYPE html>
<html lang="en">
<head>
<meta charset="utf-8">
<title>Meridell CBD – Full Spectrum CBD Oil Packaging</title>
<link rel="stylesheet" href="https://fonts.googleapis.com/css2?family=Lato:wght@300;400;700;900&display=swap">
<style>
  :root {
    --bg: #eef0f0;
    --ink-dark: #2b2929;
    --ink-black: #141414;
    --pastel: #cfe3e6;
    --pastel-deep: #b9d4d8;
    --pastel-light: #e4f0f2;
    --text-light: #e6f1f3;
    --text-muted: #9aa3a5;
    --text-dark: #3a3a3a;
  }
  * { box-sizing: border-box; margin: 0; padding: 0; }
  html, body { width: 1200px; height: 1200px; overflow: hidden; }
  body {
    background: var(--bg);
    font-family: 'Lato', sans-serif;
    position: relative;
  }

  .label, .box-panel { position: absolute; overflow: hidden; box-shadow: 0 6px 18px rgba(0,0,0,.12); }

  .dark-field { position: absolute; left: 0; right: 0; top: 0; background: var(--ink-black); }
  .box-panel .dark-field { background: var(--ink-dark); }
  .pastel-field {
    position: absolute; left: 0; right: 0; bottom: 0;
    background: linear-gradient(160deg, var(--pastel-light) 0%, var(--pastel) 55%, var(--pastel-deep) 100%);
  }

  .brand {
    position: absolute; left: 0; right: 0; text-align: center;
    color: var(--text-light);
  }
  .brand-dot {
    display: block; margin: 0 auto 14px; border-radius: 50%;
    border: 2px solid var(--text-light);
  }
  .brand-name {
    font-weight: 700; letter-spacing: .12em; text-transform: uppercase; white-space: nowrap;
  }

  .product { position: absolute; left: 0; right: 0; text-align: center; color: var(--text-dark); }
  .product-kind { font-weight: 400; text-transform: uppercase; }
  .product-name { font-weight: 900; }
  .product-strength { font-weight: 400; }
  .product-volume { font-weight: 300; color: var(--text-muted); }

  /* front label */
  .label-front { left: 80px; top: 440px; width: 250px; height: 490px; }
  .label-front .dark-field { height: 300px; }
  .label-front .pastel-field { height: 190px; }
  .label-front .brand { top: 110px; }
  .label-front .brand-dot { width: 34px; height: 34px; }
  .label-front .brand-name { font-size: 21px; }
  .label-front .product { top: 330px; }
  .label-front .product-kind { font-size: 13px; }
  .label-front .product-name { font-size: 28px; line-height: 1.15; }
  .label-front .product-strength { font-size: 21px; }
  .label-front .product-volume { font-size: 13px; margin-top: 6px; }

  /* box side */
  .box-side { left: 380px; top: 230px; width: 170px; height: 740px; }
  .box-side .dark-field { height: 500px; background: #232121; }
  .box-side .pastel-field { height: 240px; }
  .side-copy {
    position: absolute; left: 16px; right: 16px; top: 60px;
    font-size: 11.5px; line-height: 1.55; font-weight: 300; color: #bfbcbc;
    text-align: justify;
  }

  /* box front */
  .box-front { left: 550px; top: 230px; width: 280px; height: 740px; }
  .box-front .dark-field { height: 500px; }
  .box-front .pastel-field { height: 240px; }
  .box-front .brand { top: 60px; }
  .box-front .brand-dot { width: 44px; height: 44px; }
  .box-front .brand-name { font-size: 24px; }
  .box-front .product { top: 348px; color: var(--text-light); }
  .box-front .product-kind { font-size: 15px; }
  .box-front .product-name { font-size: 33px; line-height: 1.2; }
  .box-front .product-strength { font-size: 25px; }
  .box-front .product-volume { font-size: 15px; margin-top: 10px; }

  /* back label */
  .label-back { left: 870px; top: 440px; width: 250px; height: 490px; }
  .label-back .dark-field { height: 300px; }
  .label-back .pastel-field { height: 190px; }
  .back-copy {
    position: absolute; left: 18px; right: 18px;
    font-size: 12px; line-height: 1.45; font-weight: 300; text-align: justify;
  }
  .back-copy strong { font-weight: 700; font-style: italic; }
  .back-usage { top: 120px; color: var(--text-light); }
  .back-usage p + p { margin-top: 14px; }
  .back-ingredients { top: 312px; color: #4a4f50; }
  .cert-row { position: absolute; left: 18px; bottom: 22px; display: flex; gap: 10px; align-items: center; }
  .cert { width: 30px; height: 30px; border-radius: 50%; background: #3c3f40; }
  .cert-square { width: 40px; height: 24px; border-radius: 3px; }
</style>
</head>
<body>

  <section class="label label-front" aria-label="Front bottle label">
    <div class="dark-field"></div>
    <div class="pastel-field" role="img" aria-label="Pale blue topographic contour line pattern"></div>
    <div class="brand">
      <span class="brand-dot"></span>
      <span class="brand-name">Meridell CBD</span>
    </div>
    <div class="product">
      <p class="product-kind">Full Spectrum</p>
      <p class="product-name">CBD OIL</p>
      <p class="product-strength">1000 mg</p>
      <p class="product-volume">0.33 FL OZ (10 ml)</p>
    </div>
  </section>

  <section class="box-panel box-side" aria-label="Box side panel">
    <div class="dark-field"></div>
    <div class="pastel-field" role="img" aria-label="Pale blue topographic contour line pattern"></div>
    <p class="side-copy">Lorem Ipsum is simply dummy text of the printing and typesetting industry. Lorem Ipsum has been the industry's standard dummy text ever since the 1500s, when an unknown printer took a galley of type and scrambled it to make a type specimen book. It has survived not only five centuries, but also the leap into electronic typesetting, remaining essentially unchanged. It was popularised in the 1960s with the release of Tessaline sheets containing Lorem Ipsum passages, and more recently with desktop publishing software like Folio Layout including versions of Lorem Ipsum.</p>
  </section>

  <section class="box-panel box-front" aria-label="Box front panel">
    <div class="dark-field"></div>
    <div class="pastel-field" role="img" aria-label="Pale blue topographic contour line pattern"></div>
    <div class="brand">
      <span class="brand-dot"></span>
      <span class="brand-name">Meridell CBD</span>
    </div>
    <div class="product">
      <p class="product-kind">Full Spectrum</p>
      <p class="product-name">CBD OIL</p>
      <p class="product-strength">1000 mg</p>
      <p class="product-volume">0.33 FL OZ (10 ml)</p>
    </div>
  </section>

  <section class="label label-back" aria-label="Back bottle label">
    <div class="dark-field"></div>
    <div class="pastel-field" role="img" aria-label="Pale blue topographic contour line pattern"></div>
    <div class="back-copy back-usage">
      <p><strong>Dosage:</strong> Shake before use. Each spray (0.2ml) can be added direct into mouth, or a drink (hot or cold). Use 1-3 pumps, 1-2 times per day unless otherwise advised.</p>
      <p><strong>Storage info:</strong> Store in a cool place, away from direct sunlight. Do not exceed recommended dosage.</p>
    </div>
    <p class="back-copy back-ingredients"><strong>Ingredients:</strong> Water, curcumin, vegetable glycerine, echinacea, Vitamin E, myrcene, caryophyllene, Limonene, pinene, linalool, sodium bicarbonate, CBD, CBC, CBG</p>
    <div class="cert-row" aria-label="Certification marks">
      <span class="cert"></span>
      <span class="cert"></span>
      <span class="cert cert-square"></span>
    </div>
  </section>

</body>
</html>
```